Assessment Report cover design and formatting

This report is for senior executives and provides leaders with detailed insight into their capabilities and skills. The cover should have space for the date and name of the person doing the assessment. We are looking to modernise the report cover design. We would like the report to be our company colours if possible. The work will likely expand once the cover is done to other parts of the report, ie. the format and layout of the report etc.

Company colours:
Primary colours:
• Blue #0D47A1, #115CD0, #90B6ED, #EEf3FB
• Green #0D91A1, #47A10D, #324C196, #0DA11D
Additional colours:
• Purple #A10D91
• Brown #A1670D
• Red #A10D47

Target Market(s)

Executives

Industry/Entity Type

Consulting, leadership development

Colors
0094D4
00A9DD
6FCCEA
C7EBF8
E9F6FB
00AB8E
00BBA5
67D7C9
C6EFE9
E9F9F6
E54698
E96AAD
F1A4CE
F9D9EA
FCEFF6
6B429C
8869AF
B7A5CE
E3DAEB
F3F0F8

Requirements
Must have
• The report cover should have space for name of user, the date and company logo. Cover should be in A4 size.

```html
<!DOCTYPE html>
<html lang="en">
<head>
<meta charset="utf-8">
<title>Growth Leader Assessment – Report Cover</title>
<link rel="stylesheet" href="https://fonts.googleapis.com/css2?family=Montserrat:wght@400;500;600;700&display=swap">
<style>
  :root {
    --stage: #9a9b9d;
    --paper: #ffffff;
    --blue-deep: #0D47A1;
    --blue-text: #1646A0;
    --blue-mid: #115CD0;
    --blue-sky: #0094D4;
    --blue-light: #6FCCEA;
    --blue-pale: #E9F6FB;
    --green: #0DA11D;
    --green-title: #14A321;
  }
  * { box-sizing: border-box; margin: 0; padding: 0; }
  html, body {
    width: 1200px; height: 1126px; overflow: hidden;
    background: var(--stage);
    font-family: "Montserrat", sans-serif;
  }
  .cover {
    position: absolute; left: 304px; top: 97px;
    width: 624px; height: 778px;
    background: var(--paper);
    overflow: hidden;
  }
  .cover-art { position: absolute; inset: 0; }
  .title-box {
    position: absolute; left: 0; top: 79px;
    width: 300px; height: 73px;
    background: var(--paper);
    border-radius: 0 4px 4px 0;
    padding: 6px 0 0 8px;
  }
  .title-main {
    font-weight: 700; font-size: 34px; line-height: 37px;
    color: var(--blue-deep);
  }
  .title-sub {
    font-weight: 500; font-size: 30px; line-height: 30px;
    color: var(--green-title); margin-left: 2px;
  }
  .recipient {
    position: absolute; left: 24px; top: 597px;
    color: var(--blue-text);
  }
  .recipient-label { font-size: 14px; font-weight: 500; letter-spacing: 0.3px; }
  .recipient-name { font-size: 14px; font-weight: 700; letter-spacing: 0.6px; margin: 12px 0 0 24px; }
  .report-date { font-size: 14px; font-weight: 500; letter-spacing: 0.4px; margin: 23px 0 0 14px; }
  .company-name {
    position: absolute; right: 10px; top: 592px;
    width: 250px;
    text-align: right;
    font-weight: 400; font-size: 28px; line-height: 44px;
    letter-spacing: 4px; color: var(--blue-text);
  }
  .company-name span { display: block; }
  .confidential {
    position: absolute; left: 248px; top: 718px;
    font-size: 12px; font-weight: 500; letter-spacing: 0.4px;
    color: var(--blue-text);
  }
</style>
</head>
<body>
  <main class="cover">
    <svg class="cover-art" width="624" height="778" viewBox="0 0 624 778">
      <defs>
        <linearGradient id="heroFill" x1="0" y1="0" x2="1" y2="0.3">
          <stop offset="0" stop-color="#0A5FB8"/>
          <stop offset="0.35" stop-color="#0A86D6"/>
          <stop offset="0.7" stop-color="#9DDCF5"/>
          <stop offset="1" stop-color="#1A7CD0"/>
        </linearGradient>
        <linearGradient id="heroFade" x1="0" y1="0" x2="0" y2="1">
          <stop offset="0.82" stop-color="#ffffff" stop-opacity="0"/>
          <stop offset="1" stop-color="#ffffff" stop-opacity="1"/>
        </linearGradient>
      </defs>
      <rect class="top-band" x="0" y="0" width="624" height="170" fill="var(--blue-deep)"/>
      <path class="hero-art" role="img" aria-label="Abstract illustration of glowing hexagonal wireframe shapes radiating from a bright light"
            d="M0 30 C200 10 430 40 624 156 L624 572 L0 572 Z" fill="url(#heroFill)"/>
      <path d="M0 30 C200 10 430 40 624 156 L624 572 L0 572 Z" fill="url(#heroFade)"/>
      <path class="swoosh" d="M0 32 C180 18 400 28 600 146 C420 50 200 30 0 64 Z" fill="var(--green)"/>
      <path class="stripe-blue" d="M0 746 L405 746 L400 755 L0 755 Z" fill="var(--blue-deep)"/>
      <path class="stripe-green" d="M430 738 L624 738 L624 778 L0 778 L0 764 L414 764 Z" fill="var(--green)"/>
    </svg>

    <div class="title-box">
      <div class="title-main">Growth Leader</div>
      <div class="title-sub">Assessment</div>
    </div>

    <section class="recipient">
      <p class="recipient-label">INSIGHT REPORT FOR</p>
      <p class="recipient-name">CLARA BENTON</p>
      <p class="report-date">October 03, 2023</p>
    </section>

    <p class="company-name"><span>Northvale</span><span>Consulting</span></p>

    <p class="confidential">CONFIDENTIAL</p>
  </main>
</body>
</html>
```